Calorie website redesign while keeping current structure

****UPDATE****
Dear designers!

I'd really appreciate to see new color ideas.
The green-red-yellow scheme is the old scheme, and I want to change it. I asked for new colors with same structure, but I get designs with old colors and new structure. :(

My goal is to get a design with a good overall impression.
I need new color ideas where colors are in harmony and gives pleasant OVERALL impression to the eyes.

Your tools again:
1. you can use any colors (i prefer green and blue variations as the most dominant color)
2. you can use gradients
3. you can use transparency.
4. you can use background images.
5. you can change font type (but stay compatible with other languages like Hungarian)

All designs I got so far was not usable because they were not compatible with the site structure.
It was written in description we have fixed sizes, and what you can change and what you CANT change.
To make it more clear what I need I attach a picture now: understand_the_structure.jpg

Note: i dont like white color. It looks empty and it doesnt give a character to the site.

Separation: it's important the site parts to be easily separated by the eye. The site consists of 4 main parts: menu, what did you eat, what did you do, and yellow calculation boxes. They should be separated easily by looking at it.
*****END OF UPDATE****

DEAR DESIGNERS!

My name is Bence, I run this website tolvenipont.hu which is the most popular calorie counting website in Hungary with 500.000 users. It has also an English version, mealtrackly.com (started not long ago). Now you have to focus only on the mobile version main page:
https://mealtrackly.com/?layout=m

There a lot of other urgent tasks about the site and I had no chance to improve the design in the last years . But I'm aware of the problem: the website doesn't look good enough to be appealing for new users. So now I decided to run a contest to see if you can help me with this.

UNDERSTANDING CURRENT DESIGN CONCEPT:

1. The original concept of the site was that calories are "bad" so they are red color, and sport activites are "good", so they are green color. Red and green is very different color (which is advantage in separating those sections), but they don't look nice together, so I'm ready to change the colors but somehow we still need to show that calories are "bad" and sports are "good". The yellow boxes are showing calculated numbers.
2. The original concept was that I wanted the whole site to have a "calculator feeling": the message is that it is not made to attract people by fancy design, but it's strongness is it's knowledge and usability, same as a hand calculator. I want to maintain this concept, but with a more modern design.
3. Another concept is that I want to make the usability easier for long time users instead of first time users. It means I prefer to show more options/buttons on the screen (which can be frightening to new users, but it's okay), instead of having a very easy-to-use feeling when you first visit our site (but later you need to click a lot to reach functions). Number one priority is still long time usability.
4. I want to emphasise I love to use colors to separate parts.

SUMMARY:

i know it's not easy to make it look better AND compatible current structure, it's a big challenge. Be creative and use your imaginations. It's possible that I will need further adjustments from winning designer in the future, so it's a plus if you will be available to work.
You can see in my_try.png what I was trying by adding some shades, but I failed. I realized that I'm not able to create a new look (as my mind is limited to my current scheme, and I need a fresh mind for this :)).

Thanks,
Bence Fodor

I got a car accident, and couldnt leave the countryside. i cant view and review works from here. I will send u an image tomorrow afternoon showing the fixed structure, to avoid misunderstandings in future. so far none of the design is usable, because they were NOT created in our 40px size/5px space structure as i requested in posting thanks for understanding

Received designs were not compatible with structure. It was written in the description, but now I also I updated the description to give a more clear view what I need.

Target Market(s)

weight-loss

Industry/Entity Type

Weight

Number of Pages Required

1 page

Font styles to use
Sans Serif

Colors

Designer to choose colors to be used in the design.

Requirements
Must have
• WHAT CHANGES AM I EXPECTING FROM YOU?
• 1. you can use new colors totally freely along all site.
• 2. You can add some color overlays, gradients, backgrounds, to different sections.
• 3. You can add new edges (delete /increase edges) to buttons/rows (without changing the size).
• 6. If you use new font, then it should be 100% compatible with different languages (for example: Hungarian characters like ö, ő, ü, ű, etc).
• 2. I need better design for input fields (currently inactive is red, and active is white, but you can change it)
• OTHER IMPORTANT NOTES:
• 1. Be careful with technologies which could cause performance issues, as site speed is very important.
• 2. The main goal now is NOT to get new images on buttons (it's perfectly okay if you dont touch them), but an overall better and consistent look. However if you want to achieve this goal by also redesigning buttons and rows (new color, new active/press effect, ), you can do this too. In current version buttons are 40x40, but in new design they will be 80x80.
• 3. The new color concept needs to be compatible with meal colors like breakfast, dinner, etc.
• 4. I love flat design, but I want to encourage you not to limit your imagination. I really appreciate creative ideas, flat or not.
• 5. I want a mobil app athmosphere. Most of the similar sites use so simple designs that they look like settings menu of your phone. I find them very boring, I want to separate sections with nice colors (maybe backgrounds).
• 6. Clear visibility is also important so try to avoid hurting it with too many new design elements.
• 7. First I need only a picture about the new design showing the main page with added meal rows. But of course in the end I need the winning design in a format which I we can use also to sub-menus and desktop version of the site.
Should not have
• WHAT YOU SHOULD NOT CHANGE:
• The menu structure, positions, the buttons sizes. The button animations and sub-menus are all based on this structure, where we use 5px spacing, and 40px rows, and buttons (however we want to double the resolution for these ones: 10 and 80px). We cannot change this basic structure, because it needs a lot of programming, so you need to be creative to make it look better with current structure.

```html
<!DOCTYPE html>
<html lang="en">
<head>
<meta charset="utf-8">
<title>Nutri Ledger – Mobile Main Page</title>
<link rel="stylesheet" href="https://fonts.googleapis.com/css2?family=Exo+2:wght@400;500;600;700&display=swap">
<style>
  :root {
    --page: #ffffff;
    --brand-blue: #0a86f2;
    --brand-blue-soft: #5ab3f7;
    --nav-dark: #1e2836;
    --band-black: #0f151d;
    --panel: #2d3748;
    --green: #00c98d;
    --macro-green: #00d26a;
    --orange: #ff9a00;
    --purple: #7d5cf2;
    --track: #4a4f58;
    --white: #ffffff;
    --muted: #a6adb8;
    --ink: #13202b;
    --field-text: #8f949a;
  }
  * { box-sizing: border-box; margin: 0; padding: 0; }
  html, body { width: 1200px; height: 1188px; overflow: hidden; background: var(--page); }
  body { font-family: "Exo 2", sans-serif; color: var(--white); }

  .stage { position: relative; width: 1000px; height: 990px; transform: scale(1.2); transform-origin: 0 0; }
  .app { position: absolute; left: 192px; top: 105px; width: 639px; height: 885px; background: var(--nav-dark); overflow: hidden; }
  .abs { position: absolute; }

  /* header */
  .header { left: 0; top: 0; width: 639px; height: 89px; background: var(--brand-blue); }
  .brand-dot { left: 14px; top: 20px; width: 50px; height: 50px; border-radius: 50%; background: var(--brand-blue-soft); }
  .brand-name { left: 80px; top: 25px; font-size: 16px; line-height: 22px; color: #d6ebfd; font-weight: 400; }
  .tab-dot { top: 31px; width: 28px; height: 28px; border-radius: 50%; background: var(--brand-blue-soft); color: var(--white); font-size: 17px; font-weight: 600; display: flex; align-items: center; justify-content: center; }
  .menu-icon { left: 583px; top: 32px; }

  /* date nav */
  .date-nav { left: 0; top: 89px; width: 639px; height: 105px; background: var(--nav-dark); }
  .date-label { left: 0; width: 631px; top: 34px; text-align: center; font-size: 33px; font-weight: 400; }

  /* budget */
  .budget { left: 0; top: 194px; width: 639px; height: 86px; background: var(--band-black); }
  .budget-text { left: 10px; top: 14px; font-size: 33px; font-weight: 600; white-space: nowrap; }
  .budget-text .eaten { color: var(--green); }
  .budget-text .note { font-size: 18px; font-weight: 400; margin-left: 6px; }
  .budget-text .note b { color: var(--green); font-weight: 400; }
  .progress { left: 1px; top: 62px; width: 636px; height: 17px; border-radius: 9px; background: var(--track); overflow: hidden; }
  .progress-fill { width: 427px; height: 100%; border-radius: 9px; background: var(--green); }

  /* search */
  .search { left: 8px; top: 286px; width: 528px; height: 79px; background: var(--white); }
  .search-placeholder { left: 66px; top: 23px; font-size: 26px; color: var(--field-text); font-weight: 400; }
  .search-go { left: 456px; top: 9px; width: 62px; height: 62px; border-radius: 50%; background: var(--green); display: flex; align-items: center; justify-content: center; }

  .more { width: 80px; height: 79px; background: var(--panel); display: flex; align-items: center; justify-content: center; gap: 7px; }
  .more i { width: 7px; height: 7px; border-radius: 50%; background: var(--white); display: block; }

  /* quick chips */
  .chip { height: 40px; display: flex; align-items: center; justify-content: center; font-size: 14px; font-weight: 500; white-space: nowrap; }
  .chip--recent { border: 1.5px solid var(--green); color: var(--green); }
  .chip--fav { background: var(--green); color: var(--ink); }
  .chip--staple { border: 1.5px solid var(--brand-blue); color: var(--white); }
  .chip--suggest { background: var(--panel); color: var(--orange); }

  /* food rows */
  .food { left: 8px; width: 440px; height: 79px; background: var(--panel); }
  .food::after { content: ""; position: absolute; left: 0; right: 0; bottom: 0; height: 5px; }
  .food--breakfast::after { background: var(--brand-blue); }
  .food--snack::after { background: var(--green); }
  .food-name { left: 27px; top: 12px; font-size: 25px; font-weight: 400; }
  .food-weight { left: 27px; top: 44px; font-size: 19px; font-weight: 400; color: var(--muted); }
  .kcal { right: 10px; top: 6px; text-align: right; line-height: 1; }
  .kcal strong { display: block; font-size: 35px; font-weight: 600; }
  .kcal span { display: block; font-size: 20px; font-weight: 400; color: var(--muted); margin-top: 5px; }

  .meal { left: 163px; width: 285px; height: 79px; display: flex; align-items: center; padding-left: 22px; font-size: 25px; font-weight: 600; }
  .meal--breakfast { background: var(--brand-blue); }
  .meal--snack { background: var(--green); }
  .meal .kcal span { color: rgba(255,255,255,.75); font-weight: 400; }

  /* macros */
  .macros { left: 457px; width: 80px; height: 79px; display: flex; flex-direction: column; justify-content: space-between; }
  .macro { position: relative; height: 19px; background: var(--panel); font-size: 14px; font-weight: 600; }
  .macro-key { position: absolute; left: 0; top: 0; height: 19px; padding-left: 5px; line-height: 19px; color: var(--ink); }
  .macro-key--p { width: 24px; background: var(--macro-green); }
  .macro-key--c { width: 54px; background: var(--orange); }
  .macro-key--f { width: 37px; background: var(--purple); }
  .macro-val { position: absolute; right: 6px; top: 0; line-height: 19px; color: var(--white); }
</style>
</head>
<body>
<div class="stage">
  <main class="app">

    <header class="abs header">
      <div class="abs brand-dot"></div>
      <div class="abs brand-name">Nutri<br>Ledger</div>
      <div class="abs tab-dot" style="left:245px">a</div>
      <div class="abs tab-dot" style="left:302px">b</div>
      <div class="abs tab-dot" style="left:359px">c</div>
      <svg class="abs menu-icon" width="32" height="26" viewBox="0 0 32 26" aria-label="Menu">
        <g stroke="#fff" stroke-width="2.4" stroke-linecap="round">
          <line x1="2" y1="2" x2="30" y2="2"/><line x1="6" y1="13" x2="26" y2="13"/><line x1="2" y1="24" x2="30" y2="24"/>
        </g>
      </svg>
    </header>

    <nav class="abs date-nav">
      <svg class="abs" style="left:38px;top:40px" width="16" height="30" viewBox="0 0 16 30" aria-label="Previous day">
        <polyline points="14,2 2,15 14,28" fill="none" stroke="#0a86f2" stroke-width="3" stroke-linecap="round"/>
      </svg>
      <div class="abs date-label">Today</div>
      <svg class="abs" style="left:467px;top:38px" width="30" height="32" viewBox="0 0 30 32" aria-label="Calendar">
        <g fill="none" stroke="#fff" stroke-width="2.2" stroke-linecap="round">
          <rect x="2" y="5" width="26" height="25" rx="5"/><line x1="2" y1="13" x2="28" y2="13"/>
          <line x1="9" y1="1" x2="9" y2="8"/><line x1="21" y1="1" x2="21" y2="8"/>
        </g>
      </svg>
      <svg class="abs" style="left:583px;top:40px" width="16" height="30" viewBox="0 0 16 30" aria-label="Next day">
        <polyline points="2,2 14,15 2,28" fill="none" stroke="#0a86f2" stroke-width="3" stroke-linecap="round"/>
      </svg>
    </nav>

    <section class="abs budget">
      <div class="abs budget-text"><span class="eaten">1500</span>/2500<span class="note">you can eat <b>1000</b> more kcal today</span></div>
      <svg class="abs" style="left:577px;top:19px" width="34" height="34" viewBox="0 0 34 34" aria-label="Settings">
        <g fill="#fff">
          <circle cx="17" cy="17" r="11"/>
          <rect x="14" y="0" width="6" height="8" rx="1"/><rect x="14" y="26" width="6" height="8" rx="1"/>
          <rect x="0" y="14" width="8" height="6" rx="1"/><rect x="26" y="14" width="8" height="6" rx="1"/>
          <g transform="rotate(45 17 17)">
            <rect x="14" y="0" width="6" height="8" rx="1"/><rect x="14" y="26" width="6" height="8" rx="1"/>
            <rect x="0" y="14" width="8" height="6" rx="1"/><rect x="26" y="14" width="8" height="6" rx="1"/>
          </g>
        </g>
        <circle cx="17" cy="17" r="6" fill="#0f151d"/>
      </svg>
      <div class="abs progress"><div class="progress-fill"></div></div>
    </section>

    <div class="abs search">
      <svg class="abs" style="left:22px;top:28px" width="30" height="22" viewBox="0 0 30 22" aria-label="Meal">
        <g fill="none" stroke="#8f949a" stroke-width="2" stroke-linecap="round">
          <path d="M4 17 A11 11 0 0 1 26 17"/><line x1="1" y1="19" x2="29" y2="19"/><line x1="15" y1="2" x2="15" y2="5"/>
        </g>
      </svg>
      <div class="abs search-placeholder">What did you eat?</div>
      <svg class="abs" style="left:418px;top:26px" width="26" height="28" viewBox="0 0 26 28" aria-label="Sort">
        <g stroke="#8f949a" stroke-width="2" stroke-linecap="round" fill="none">
          <line x1="5" y1="2" x2="5" y2="25"/><polyline points="1,21 5,26 9,21"/>
          <line x1="12" y1="3" x2="25" y2="3"/><line x1="12" y1="9" x2="23" y2="9"/>
          <line x1="12" y1="15" x2="21" y2="15"/><line x1="12" y1="21" x2="19" y2="21"/>
        </g>
      </svg>
      <div class="abs search-go">
        <svg width="32" height="32" viewBox="0 0 32 32" aria-label="Search">
          <g fill="none" stroke="#fff" stroke-width="2.6" stroke-linecap="round">
            <circle cx="13" cy="13" r="10"/><line x1="20.5" y1="20.5" x2="29" y2="29"/>
          </g>
        </svg>
      </div>
    </div>
    <div class="abs more" style="left:547px;top:286px"><i></i><i></i><i></i></div>

    <div class="abs chip chip--recent" style="left:8px;top:377px;width:115px">White bread</div>
    <div class="abs chip chip--recent" style="left:134px;top:377px;width:116px">Tomatoes</div>
    <div class="abs chip chip--fav" style="left:259px;top:377px;width:116px">Apples</div>
    <div class="abs chip chip--fav" style="left:385px;top:377px;width:117px">Grapes</div>
    <div class="abs chip chip--fav" style="left:511px;top:377px;width:116px">Potato</div>
    <div class="abs chip chip--staple" style="left:8px;top:427px;width:115px">Corn</div>
    <div class="abs chip chip--staple" style="left:134px;top:427px;width:116px">Pasta</div>
    <div class="abs chip chip--suggest" style="left:259px;top:427px;width:116px">Protein bar</div>
    <div class="abs chip chip--suggest" style="left:385px;top:427px;width:117px">Black beans...</div>
    <div class="abs chip chip--suggest" style="left:511px;top:427px;width:116px">Egg</div>

    <div class="abs food food--breakfast" style="top:476px">
      <div class="abs food-name">Cheese Sandwich</div>
      <div class="abs food-weight">300 gr</div>
      <div class="abs kcal"><strong>460</strong><span>kcal</span></div>
    </div>
    <div class="abs macros" style="top:476px">
      <div class="macro"><span class="macro-key macro-key--p">P:</span><span class="macro-val">10</span></div>
      <div class="macro"><span class="macro-key macro-key--c">C:</span><span class="macro-val">50</span></div>
      <div class="macro"><span class="macro-key macro-key--f">F:</span><span class="macro-val">35</span></div>
    </div>
    <div class="abs more" style="left:547px;top:476px"><i></i><i></i><i></i></div>

    <div class="abs meal meal--breakfast" style="top:566px">Breakfast
      <div class="abs kcal"><strong>460</strong><span>kcal</span></div>
    </div>
    <div class="abs macros" style="top:566px">
      <div class="macro"><span class="macro-key macro-key--p">P:</span><span class="macro-val">10</span></div>
      <div class="macro"><span class="macro-key macro-key--c">C:</span><span class="macro-val">50</span></div>
      <div class="macro"><span class="macro-key macro-key--f">F:</span><span class="macro-val">35</span></div>
    </div>
    <div class="abs more" style="left:547px;top:566px"><i></i><i></i><i></i></div>

    <div class="abs food food--snack" style="top:656px">
      <div class="abs food-name">Apple</div>
      <div class="abs food-weight">150 gr</div>
      <div class="abs kcal"><strong>60</strong><span>kcal</span></div>
    </div>
    <div class="abs macros" style="top:656px">
      <div class="macro"><span class="macro-key macro-key--p">P:</span><span class="macro-val">10</span></div>
      <div class="macro"><span class="macro-key macro-key--c">C:</span><span class="macro-val">50</span></div>
      <div class="macro"><span class="macro-key macro-key--f">F:</span><span class="macro-val">35</span></div>
    </div>
    <div class="abs more" style="left:547px;top:656px"><i></i><i></i><i></i></div>

    <div class="abs meal meal--snack" style="top:746px">Mid-morning
      <div class="abs kcal"><strong>60</strong><span>kcal</span></div>
    </div>
    <div class="abs macros" style="top:746px">
      <div class="macro"><span class="macro-key macro-key--p">P:</span><span class="macro-val">10</span></div>
      <div class="macro"><span class="macro-key macro-key--c" style="width:36px">C:</span><span class="macro-val">50</span></div>
      <div class="macro"><span class="macro-key macro-key--f">F:</span><span class="macro-val">35</span></div>
    </div>
    <div class="abs more" style="left:547px;top:746px"><i></i><i></i><i></i></div>

    <div class="abs food" style="top:836px">
      <div class="abs food-name">Cesar Salad</div>
      <div class="abs kcal"><strong>150</strong><span>kcal</span></div>
    </div>
    <div class="abs macros" style="top:836px">
      <div class="macro"><span class="macro-key macro-key--p">P:</span><span class="macro-val">10</span></div>
      <div class="macro"><span class="macro-key macro-key--c" style="width:32px;border-radius:8px">C:</span><span class="macro-val">50</span></div>
      <div class="macro"><span class="macro-key macro-key--f">F:</span><span class="macro-val">35</span></div>
    </div>
    <div class="abs more" style="left:547px;top:836px"><i></i><i></i><i></i></div>

  </main>
</div>
</body>
</html>
```